Medical Billing Company Needs a Business Card Design

We need a business card design for a Florida based medical billing company called 'Medora Crestline Solutions'. We specialize in providing revenue cycle management services to physician and therapist offices (we're basically their back-office processing partner for providing billing software, claims submissions, A/R follow-up and patient statements & collections. Our logo is red and blue-ish, so make sure that whatever other elements are used will match appropriately. Our current business card design has a too small font size. I'd like to project an image that shows we are modern & reliable. On a side note, I'm planning on using ZIB for printing these cards.

Target Market(s)

Office managers, physicians, therapists

Industry/Entity Type

Printing

Requirements
Must have
• Logo
Name of Employee
Phone
Fax
E-mail
Website

```html
<!DOCTYPE html>
<html lang="en">
<head>
<meta charset="utf-8">
<title>Medora Crestline Solutions – Business Card</title>
<link rel="stylesheet" href="https://fonts.googleapis.com/css2?family=Mulish:wght@700&family=Questrial&display=swap">
<style>
  :root {
    --backdrop: #3c3c3e;
    --paper: #f6f6f4;
    --navy: #1c1350;
    --navy-deep: #150e3e;
    --brand-navy: #2a1d6b;
    --crimson: #9b1b22;
    --ink-light: #e9e8f2;
  }
  * { margin: 0; padding: 0; box-sizing: border-box; }
  html, body {
    width: 1200px; height: 1000px; overflow: hidden;
    background: var(--backdrop);
    font-family: "Questrial", "Century Gothic", sans-serif;
  }
  .canvas { position: relative; width: 1200px; height: 1000px; }
  .card {
    position: absolute;
    width: 498px; height: 326px;
    background: var(--paper);
    box-shadow: 0 4px 10px rgba(0,0,0,.35);
    overflow: hidden;
  }
  .card--front { left: 172px; top: 128px; }
  .card--back { left: 534px; top: 533px; width: 496px; height: 325px; }
  .card__shapes { position: absolute; inset: 0; width: 100%; height: 100%; }
  .wordmark {
    position: absolute; left: 0; right: 0;
    text-align: center;
    font-family: "Questrial", "Century Gothic", sans-serif;
    font-size: 24px; letter-spacing: 1.2px;
    color: var(--brand-navy);
    white-space: nowrap;
  }
  .card--front .wordmark { top: 54px; }
  .card--back .wordmark { top: 143px; }
  .contact-list {
    position: absolute; left: 34px; top: 228px;
    list-style: none;
    color: var(--ink-light);
    font-size: 12.5px; line-height: 17.5px;
  }
  .contact-list li { display: flex; align-items: center; gap: 7px; }
  .contact-list svg { width: 14px; height: 14px; flex: none; }
  .person {
    position: absolute; right: 35px; top: 206px;
    text-align: right; color: var(--ink-light);
  }
  .person__name {
    font-family: "Mulish", "Century Gothic", sans-serif;
    font-weight: 700; font-size: 18px; letter-spacing: .5px;
    color: #ffffff;
  }
  .person__role { font-size: 14px; margin-top: 1px; }
  .person__address { font-size: 12px; line-height: 18px; margin-top: 20px; }
</style>
</head>
<body>
<main class="canvas">

  <section class="card card--front" aria-label="Business card front">
    <svg class="card__shapes" viewBox="0 0 498 326" preserveAspectRatio="none" aria-hidden="true">
      <path d="M0,143 Q240,180 498,152 L498,156 Q240,172 0,152 Z" fill="var(--crimson)"/>
      <path d="M0,158 Q240,182 498,157 L498,326 L0,326 Z" fill="var(--navy)"/>
    </svg>
    <div class="wordmark">MEDORA CRESTLINE SOLUTIONS</div>

    <ul class="contact-list">
      <li>
        <svg viewBox="0 0 14 14"><circle cx="7" cy="7" r="6.2" fill="none" stroke="currentColor"/><path d="M4.6 3.8l1.3 1.4-.7 1a4.5 4.5 0 0 0 2.6 2.6l1-.7 1.4 1.3-.9 1c-2.7-.3-5.3-2.9-5.6-5.6z" fill="currentColor"/></svg>
        555 210 4837
      </li>
      <li>
        <svg viewBox="0 0 14 14"><circle cx="7" cy="7" r="6.2" fill="none" stroke="currentColor"/><rect x="4.8" y="3.6" width="4.4" height="2.4" fill="currentColor"/><rect x="3.6" y="6.2" width="6.8" height="3" rx=".6" fill="currentColor"/><rect x="4.8" y="8.4" width="4.4" height="2" fill="none" stroke="currentColor" stroke-width=".8"/></svg>
        555 210 4838
      </li>
      <li>
        <svg viewBox="0 0 14 14"><circle cx="7" cy="7" r="6.2" fill="none" stroke="currentColor"/><rect x="3.8" y="4.8" width="6.4" height="4.4" fill="currentColor"/><path d="M3.8 4.8L7 7.4l3.2-2.6" fill="none" stroke="var(--navy)" stroke-width=".8"/></svg>
        info@medoracrestline.net
      </li>
      <li>
        <svg viewBox="0 0 14 14" fill="none" stroke="currentColor" stroke-width=".9"><circle cx="7" cy="7" r="6.2"/><ellipse cx="7" cy="7" rx="2.6" ry="6.2"/><path d="M.8 7h12.4M2 4h10M2 10h10"/></svg>
        www.medoracrestline.net
      </li>
    </ul>

    <div class="person">
      <div class="person__name">ELENA MARSH</div>
      <div class="person__role">Manager</div>
      <div class="person__address">2760 SE Harbor Road<br>Port Larkin, FL 34000</div>
    </div>
  </section>

  <section class="card card--back" aria-label="Business card back">
    <svg class="card__shapes" viewBox="0 0 496 325" preserveAspectRatio="none" aria-hidden="true">
      <path d="M0,0 L496,0 L496,101 Q250,76 0,99 Z" fill="var(--navy-deep)"/>
      <path d="M0,102 Q250,78 496,104 L496,110 Q250,86 0,106 Z" fill="var(--crimson)"/>
      <path d="M0,212 Q250,238 496,220 L496,225 Q250,236 0,219 Z" fill="var(--crimson)"/>
      <path d="M0,224 Q250,246 496,229 L496,325 L0,325 Z" fill="var(--navy-deep)"/>
    </svg>
    <div class="wordmark">MEDORA CRESTLINE SOLUTIONS</div>
  </section>

</main>
</body>
</html>
```